Double caffeinated coffee label design

We need to design labels for a new coffee brand. The label size: 2.75” x 4.125” (Corners slightly rounded). There will be front and back label in stickers to be put on standardized bags. Our product is roasted whole bean and ground coffee in 12oz bags. It is described as "strong, bold, intense, and double caffeinated. The product is designed for passionate coffee drinkers who want strong, more caffeinated but not bitter coffee. The coffee is suitable for espresso base coffees.
Target Market(s)
Groceries, food stores, super markets. Heavy and sophisticated coffee drinkers.
Requirements
Must have
- Modern, minimalist style. Strong and bold look. Creative. Impressive.
Nice to have
- Some impressed coffee label designs for reference: https://www.vistrelo.net/find?q=most+impressive+coffee+brand+designs&src=menu&mode=img&ref=X&key=7hQpLmZrT2wXvBn4KcYsDfGaJuEo9RtMiHb3NqVe&w=1280&h=610#pic=kR4mTwXzNpQbLs:

```html
<!DOCTYPE html>
<html lang="en">
<head>
<meta charset="utf-8">
<title>Brava Roasted Whole Bean Coffee – Label Designs</title>
<link rel="stylesheet" href="https://fonts.googleapis.com/css2?family=Oswald:wght@400;600&display=swap">
<style>
  :root {
    --stage: #222222;
    --orange: #db7530;
    --orange-deep: #b9531a;
    --ink: #121212;
    --charcoal: #2a2a2a;
    --paper: #f2f2f2;
  }
  html, body {
    margin: 0;
    width: 1200px;
    height: 1200px;
    overflow: hidden;
    background: var(--stage);
  }
  .canvas {
    position: relative;
    width: 1200px;
    height: 1200px;
  }
  .label {
    position: absolute;
    top: 327px;
    width: 438px;
    height: 655px;
  }
  .label--orange { left: 84px; }
  .label--black { left: 675px; }
  .label svg { display: block; width: 100%; height: 100%; }
  .label text {
    font-family: "Oswald", "Arial Narrow", sans-serif;
    font-weight: 600;
  }
  .label .brand-sub {
    font-weight: 400;
    letter-spacing: 4px;
  }
</style>
</head>
<body>
<div class="canvas">

  <!-- Orange edition -->
  <div class="label label--orange">
    <svg viewBox="0 0 438 655" xmlns="http://www.w3.org/2000/svg" aria-label="Brava roasted whole bean coffee label, orange edition">
      <defs>
        <linearGradient id="ornament-orange" x1="0" y1="0" x2="1" y2="1">
          <stop offset="0" stop-color="#121212"/>
          <stop offset="1" stop-color="#b9531a"/>
        </linearGradient>
      </defs>
      <rect class="top-band" x="0" y="0" width="438" height="132" fill="var(--ink)"/>
      <rect class="face" x="0" y="132" width="438" height="523" fill="var(--orange)"/>
      <rect class="name-band" x="108" y="348" width="330" height="82" fill="var(--orange-deep)"/>
      <path class="ornament" role="img" aria-label="Decorative swirl ornament in black"
            d="M0 150 H100 V440 H438 V655 H0 Z" fill="url(#ornament-orange)"/>
      <circle class="brand-dot" cx="186" cy="197" r="7" fill="var(--ink)"/>
      <text class="brand" x="262" y="215" text-anchor="middle" font-size="44" fill="var(--ink)">BRAVA</text>
      <text class="brand-sub" x="262" y="241" text-anchor="middle" font-size="15" fill="var(--ink)">COFFEE</text>
      <text class="claim" x="175" y="300" font-size="46" textLength="172" lengthAdjust="spacingAndGlyphs" fill="var(--ink)">ROASTED</text>
      <text class="claim-sub" x="175" y="339" font-size="33" textLength="170" lengthAdjust="spacingAndGlyphs" fill="var(--ink)">WHOLE BEAN</text>
      <text class="product" x="176" y="410" font-size="58" textLength="168" lengthAdjust="spacingAndGlyphs" fill="var(--ink)">COFFEE</text>
    </svg>
  </div>

  <!-- Black edition -->
  <div class="label label--black">
    <svg viewBox="0 0 438 655" xmlns="http://www.w3.org/2000/svg" aria-label="Brava roasted whole bean coffee label, black edition">
      <defs>
        <linearGradient id="ornament-black" x1="0" y1="0" x2="1" y2="1">
          <stop offset="0" stop-color="#db7530"/>
          <stop offset="1" stop-color="#2a2a2a"/>
        </linearGradient>
      </defs>
      <rect class="top-band" x="0" y="0" width="438" height="132" fill="var(--orange)"/>
      <rect class="face" x="0" y="132" width="438" height="523" fill="var(--ink)"/>
      <rect class="name-band" x="108" y="348" width="330" height="82" fill="var(--charcoal)"/>
      <path class="ornament" role="img" aria-label="Decorative swirl ornament in orange"
            d="M0 150 H100 V440 H438 V655 H0 Z" fill="url(#ornament-black)"/>
      <circle class="brand-dot" cx="186" cy="197" r="7" fill="var(--orange)"/>
      <text class="brand" x="262" y="215" text-anchor="middle" font-size="44" fill="var(--orange)">BRAVA</text>
      <text class="brand-sub" x="262" y="241" text-anchor="middle" font-size="15" fill="var(--paper)">COFFEE</text>
      <text class="claim" x="175" y="300" font-size="46" textLength="172" lengthAdjust="spacingAndGlyphs" fill="var(--orange)">ROASTED</text>
      <text class="claim-sub" x="175" y="339" font-size="33" textLength="170" lengthAdjust="spacingAndGlyphs" fill="var(--orange)">WHOLE BEAN</text>
      <text class="product" x="176" y="410" font-size="58" textLength="168" lengthAdjust="spacingAndGlyphs" fill="var(--orange)">COFFEE</text>
    </svg>
  </div>

</div>
</body>
</html>
```